50c wing mondays

We need a sign reading the following.

HEADING: (large font as the focus of the sign)

50c wing Mondays
from 6pm till late

Medium font under the picture

YOUR CHOICE
- spiced buffalo wings
- hickory smoked BBQ
- Peri Peri

Small font
conditions apply
- minimum 4 wings per serving (of the same type)
- dine in only
- no discount apply

Target Market(s)

age 18 - 35

Logo Text

50c wing Mondays

Logo styles of interest
Character Logo
Font styles to use
Other font styles liked:
• chalkduster

Colors
000000
f37122
ffffff

Requirements
Must have
• Our logo
• A picture of wings
• FONT: chalkduster
• Background: BLACK
• Font colour: ORANGE
• Logo: Attached pickle wagon logo
• every word ive stated in the project description
Nice to have
• HEADING MUST BE LARGE: 50c Extra large - - - WING MONDAYS: LARGE
• The rest of the working small
Should not have
• clip art - too many colours

```html
<!DOCTYPE html>
<html lang="en">
<head>
<meta charset="utf-8">
<title>50¢ Wing Mondays</title>
<link rel="stylesheet" href="https://fonts.googleapis.com/css2?family=Cabin+Sketch:wght@400;700&family=Cabin:wght@500;700&display=swap">
<style>
  :root {
    --paper: #ffffff;
    --board: #000000;
    --orange: #f37122;
    --orange-deep: #b9521a;
    --chalk: #ffffff;
    --chalk-soft: #d9d9d9;
  }
  * { margin: 0; padding: 0; box-sizing: border-box; }
  html, body { width: 844px; height: 1200px; overflow: hidden; background: var(--paper); }
  .poster { position: relative; width: 844px; height: 1200px; background: var(--paper); }
  .poster__field {
    position: absolute; left: 15px; top: 12px; width: 820px; height: 1172px;
    background: var(--board);
    clip-path: polygon(0.4% 0.6%, 12% 0.2%, 30% 0.7%, 52% 0.1%, 74% 0.6%, 99.6% 0%, 99.2% 20%, 100% 45%, 99.3% 70%, 99.8% 99.5%, 70% 99.2%, 45% 100%, 20% 99.3%, 0% 99.8%, 0.6% 75%, 0% 50%, 0.7% 25%);
  }
  .centered { position: absolute; left: 0; width: 844px; text-align: center; }
  .price {
    top: 34px; font-family: "Cabin Sketch", cursive; font-weight: 700;
    font-size: 132px; line-height: 1; color: var(--orange);
    transform: rotate(-4deg);
  }
  .headline {
    font-family: "Cabin Sketch", cursive; font-weight: 700;
    font-size: 150px; line-height: 1; color: var(--orange);
  }
  .headline--wing { top: 176px; }
  .headline--days { top: 322px; }
  .hours {
    top: 482px; font-family: "Cabin Sketch", cursive; font-weight: 700;
    font-size: 30px; letter-spacing: 4px; color: var(--chalk);
  }
  .mascot {
    position: absolute; left: 262px; top: 552px; width: 320px; height: 290px;
    border-radius: 24px;
    background: linear-gradient(160deg, var(--orange) 0%, var(--orange-deep) 100%);
  }
  .ribbon { position: absolute; left: 137px; top: 853px; width: 572px; height: 88px; }
  .ribbon__label {
    top: 864px; font-family: "Cabin Sketch", cursive; font-weight: 700;
    font-size: 36px; line-height: 40px; letter-spacing: 4px; color: var(--board);
  }
  .choices {
    top: 936px; list-style: none; font-family: "Cabin Sketch", cursive; font-weight: 700;
    font-size: 42px; line-height: 48px; color: var(--chalk);
  }
  .conditions {
    top: 1092px; font-family: "Cabin", sans-serif; font-weight: 500;
    font-size: 13px; line-height: 16px; color: var(--chalk-soft);
  }
</style>
</head>
<body>
  <main class="poster">
    <div class="poster__field"></div>

    <div class="centered price">50¢</div>
    <h1 class="centered headline headline--wing">WING</h1>
    <div class="centered headline headline--days">MONDAYS</div>
    <p class="centered hours">FROM 6PM TILL LATE</p>

    <div class="mascot" role="img" aria-label="Illustration of a hen standing in profile"></div>

    <svg class="ribbon" viewBox="0 0 572 88" aria-hidden="true">
      <polygon points="0,27 70,27 70,87 22,87 36,57" fill="var(--orange-deep)"/>
      <polygon points="572,27 502,27 502,87 550,87 536,57" fill="var(--orange-deep)"/>
      <rect x="48" y="0" width="476" height="60" fill="var(--orange)"/>
    </svg>
    <h2 class="centered ribbon__label">YOUR CHOICE</h2>

    <ul class="centered choices">
      <li>BUFFALO SPICE WINGS</li>
      <li>HICKORY SMOKED BBQ</li>
      <li>PERI PERI</li>
    </ul>

    <div class="centered conditions">
      <p>conditions apply:</p>
      <p>minimum 4 wings per serving (of the same type)</p>
      <p>- dine in only</p>
      <p>- no discount apply</p>
    </div>
  </main>
</body>
</html>
```